Boutique Film/TV Company needs Business Card Design

Please see our website for background on our company and look of our current logo: www.lumarocpictures.ca

Pantone 314U is our main colour.

Target Market(s)

Network of peers, funders and broadcasters.

Industry/Entity Type

Business

Requirements
Must have
• We would like rounded corners and the height of the card to be shorter than traditional (maybe?!)

It's important that we have room for our office address, office number, cell number, email address, website, facebook and linked-in info (though not all of us have a linked-in account).

Would like the logo to keep the exclamation marks over the letters but the tag line/tag words of "film - television - interactive" can stay or go or... surprise me!

Nice to have
• Silky matte finish.

We are open to a change in the font of our logo/name.

```html
<!DOCTYPE html>
<html lang="en">
<head>
<meta charset="utf-8">
<title>Lumaroc Pictures – Business Card</title>
<link rel="stylesheet" href="https://fonts.googleapis.com/css2?family=Ubuntu:wght@300;400;500;700&display=swap">
<style>
  :root {
    --bg: #e6ebed;
    --card-light: #1f8dab;
    --card-dark: #10708d;
    --ink: #ffffff;
    --ink-soft: rgba(255,255,255,0.85);
    --rule: rgba(255,255,255,0.18);
  }
  * { margin: 0; padding: 0; box-sizing: border-box; }
  html, body { width: 1200px; height: 960px; overflow: hidden; }
  body {
    background: var(--bg);
    font-family: "Ubuntu", sans-serif;
    color: var(--ink);
    display: flex;
    flex-direction: column;
    align-items: center;
    justify-content: center;
    gap: 70px;
  }
  .card {
    position: relative;
    width: 840px;
    height: 330px;
    border-radius: 46px;
    background: linear-gradient(135deg, var(--card-light) 0%, var(--card-dark) 100%);
    box-shadow: 0 8px 24px rgba(0,0,0,0.12);
    overflow: hidden;
  }

  /* Contact side */
  .card-contact .holder {
    position: absolute;
    left: 62px;
    top: 70px;
    font-size: 38px;
    font-weight: 400;
  }
  .card-contact .holder .role {
    font-size: 26px;
    font-weight: 300;
  }
  .card-contact .divider {
    position: absolute;
    left: 0; right: 0;
    top: 150px;
    height: 1px;
    background: var(--rule);
  }
  .contact-list {
    position: absolute;
    left: 62px;
    top: 186px;
    list-style: none;
  }
  .contact-list li {
    display: flex;
    align-items: center;
    height: 32px;
    font-size: 24px;
    font-weight: 400;
  }
  .contact-list svg {
    width: 18px;
    height: 18px;
    margin-right: 22px;
    flex: none;
  }
  .office-address {
    position: absolute;
    left: 520px;
    top: 176px;
    font-style: normal;
    font-size: 21px;
    line-height: 28px;
    color: var(--ink-soft);
  }
  .office-address .company {
    font-weight: 700;
    color: var(--ink);
  }

  /* Brand side */
  .card-brand {
    display: flex;
    flex-direction: column;
    align-items: center;
    justify-content: center;
  }
  .brand-name {
    font-size: 104px;
    font-weight: 400;
    line-height: 1;
    letter-spacing: 0.01em;
  }
  .brand-web {
    margin-top: 36px;
    font-size: 22px;
    font-weight: 400;
    letter-spacing: 0.42em;
    padding-left: 0.42em;
  }
</style>
</head>
<body>

  <section class="card card-contact">
    <h1 class="holder">Nadia Okafor <span class="role">/ Manager</span></h1>
    <div class="divider"></div>

    <ul class="contact-list">
      <li>
        <svg viewBox="0 0 18 18" aria-hidden="true"><path fill="#fff" d="M4 1.5l3 3-1.6 2a10 10 0 0 0 6.1 6.1l2-1.6 3 3-2.2 2.2C8.8 16 2 9.2 1.8 3.7z"/></svg>
        416.555.0142
      </li>
      <li>
        <svg viewBox="0 0 18 18" aria-hidden="true"><rect x="4.5" y="1" width="9" height="16" rx="1.5" fill="#fff"/><rect x="6" y="3" width="6" height="6" fill="#1a82a0"/><rect x="6" y="11" width="6" height="4" fill="#1a82a0"/></svg>
        416.555.0187
      </li>
      <li>
        <svg viewBox="0 0 18 18" aria-hidden="true"><rect x="1" y="4" width="16" height="11" rx="1" fill="#fff"/><path d="M1.5 4.5L9 10l7.5-5.5" fill="none" stroke="#1a82a0" stroke-width="1.4"/></svg>
        nadia@lumarocpictures.ca
      </li>
      <li>
        <svg viewBox="0 0 18 18" aria-hidden="true"><rect x="2" y="2" width="14" height="14" rx="2" fill="#fff"/></svg>
        /lumarocpictures.com
      </li>
    </ul>

    <address class="office-address">
      <span class="company">Lumaroc Pictures Inc.</span><br>
      42 Alder Crescent<br>
      Toronto, ON, M4K 2B9
    </address>
  </section>

  <section class="card card-brand">
    <div class="brand-name">Lumaroc</div>
    <div class="brand-web">www.lumarocpictures.ca</div>
  </section>

</body>
</html>
```